Organic Food Producer Needs Business Card

We need an attractive business card that is both trendy and professional. We are a FQRB, Vetra Clear Certified organic producer of coconut oil, coconut flour and additional cacao products. We produce some of the world's purest coconut oil and coconut oil derived products in the world.
We take pride in the purity of our products and the transparency with which we create our products. Use of FQRB Organic and Vetra Clear logos is acceptable and preferred. The final design would reflect our values for purity and the natural state of our products.
The business card should include: job title, email address, phone number and facebook, twitter, instagram tag.
Don't be afraid to get creative! I have attached some of our packaging design in JPG format as well as our logo. The jpgs dont display the colors correctly in chrome but they will display correctly if you DL and open them in photoshop.
Target Market(s)
Cards likely to be used in organic food industry events for people such as buyers, trade show reps, etc... but also store owners and people casually interested in.
The company's target market :
Primary:
Women - 22-65. Women typically hold the household budget and make the purchasing decisions at the supermarket. They are interested in quality healthy and beauty products at a good value. Organic, fair trade, artisanally made are all important attributes of brands they purchase. They try to maintain a healthy lifestyle through proper eating, exercise and work/life balance.
Secondary:
Men - 44% of American adults are single so it is important to note that men will also be a key target audience. And they too are concerned and passionate about organic, fair trade, artisanally made, good value and living a healthy lifestyle.
Tertiary:
Health & Wellness Professionals (Nutritionists, Doctors, etc) Coconut is highly nutritional and more and more, it is being recommended as part of a healthy diet by professionals. We should keep this audience in mind as well, particularly when we build a website with useful resources such as the company’s high standards, the health benefits of coconut, nutrition info and recipes.
Industry/Entity Type
Business
Requirements
Must have
- Pretty open minded about creativity and variety, I do like the color palettes in the labeling files provided... but it is not a deal breaker to vary from this.
Should be visually impacting.
Nice to have
- Would like to have some creative use of raised lettering or detail.
Should not have
- Although the company is based in the caribbean, we are not looking for an overly ethnic caribbean feel.
You should open the attached files in photoshop, as they seem to distort the color in a web browser.

```html
<!DOCTYPE html>
<html lang="en">
<head>
<meta charset="utf-8">
<title>isla grove — business card</title>
<link rel="stylesheet" href="https://fonts.googleapis.com/css2?family=Source+Sans+3:wght@400;600&display=swap">
<style>
  :root {
    --cocoa: #3e2410;
    --lagoon: #0089a8;
    --cream: #fde3b6;
    --paper: #ffffff;
    --shadow: rgba(0, 0, 0, 0.35);
  }
  html, body {
    margin: 0;
    padding: 0;
    width: 916px;
    height: 1200px;
    overflow: hidden;
    background: var(--paper);
    font-family: "Source Sans 3", "Myriad Pro", sans-serif;
  }
  .sheet { position: relative; width: 916px; height: 1200px; }
  .card {
    position: absolute;
    overflow: hidden;
    box-shadow: 4px 5px 6px var(--shadow);
  }
  .card svg { position: absolute; left: 0; top: 0; }
  .card-front { left: 80px; top: 58px; width: 748px; height: 492px; background: var(--cocoa); }
  .card-back { left: 82px; top: 610px; width: 746px; height: 493px; background: var(--cream); }

  .brand {
    position: absolute;
    left: 108px; top: 200px;
    width: 350px;
    text-align: center;
    color: var(--cream);
  }
  .brand-row { display: flex; align-items: center; justify-content: center; gap: 16px; }
  .brand-dot { width: 40px; height: 40px; border-radius: 50%; background: var(--lagoon); }
  .brand-name { font-size: 60px; font-weight: 400; line-height: 1; letter-spacing: 1px; }
  .brand-tagline {
    margin-top: 10px;
    font-size: 19px;
    font-weight: 600;
    letter-spacing: 1.5px;
    color: var(--lagoon);
  }

  .emblem-name {
    position: absolute;
    left: 46px; top: 202px;
    width: 310px;
    text-align: center;
    font-size: 40px;
    color: var(--cream);
  }
  .badge { position: absolute; }
  .badge-square { left: 543px; top: 33px; width: 78px; height: 50px; background: var(--lagoon); border: 2px solid #ffffff; box-shadow: 0 0 0 1px #cfc5b0; }
  .badge-circle { left: 640px; top: 34px; width: 46px; height: 46px; border-radius: 50%; background: #ffffff; border: 2px solid var(--cocoa); }

  .person-name {
    position: absolute; left: 401px; top: 207px;
    margin: 0; font-size: 33px; font-weight: 400; color: var(--cream);
  }
  .person-title {
    position: absolute; left: 401px; top: 264px;
    margin: 0; font-size: 18px; color: var(--cream);
  }
  .contact {
    position: absolute; left: 401px; top: 312px;
    font-size: 16px; line-height: 21.5px; color: var(--cocoa);
  }
  .contact .phone { font-size: 33px; line-height: 38px; color: var(--lagoon); }
  .contact .label { color: var(--lagoon); }
  .contact p { margin: 0; }
</style>
</head>
<body>
<main class="sheet">

  <section class="card card-front" aria-label="Card front">
    <svg width="748" height="492" viewBox="0 0 748 492" aria-hidden="true">
      <circle cx="930" cy="246" r="378" fill="var(--lagoon)"/>
      <circle cx="930" cy="246" r="360" fill="var(--cream)"/>
      <circle cx="930" cy="246" r="346" fill="var(--lagoon)"/>
    </svg>
    <div class="brand">
      <div class="brand-row">
        <span class="brand-dot"></span>
        <span class="brand-name">isla grove</span>
      </div>
      <div class="brand-tagline">handcrafted in the caribbean</div>
    </div>
  </section>

  <section class="card card-back" aria-label="Card back">
    <svg width="746" height="493" viewBox="0 0 746 493" aria-hidden="true">
      <circle cx="-190" cy="250" r="360" fill="var(--cocoa)"/>
      <circle cx="-190" cy="250" r="340" fill="var(--cream)"/>
      <circle cx="-190" cy="250" r="322" fill="var(--cocoa)"/>
      <rect x="200" y="190" width="546" height="70" fill="var(--cocoa)"/>
      <rect x="200" y="262" width="546" height="26" fill="var(--lagoon)"/>
      <circle cx="201" cy="225" r="156" fill="var(--lagoon)"/>
    </svg>
    <div class="emblem-name">isla grove</div>
    <div class="badge badge-square" aria-label="Vetra Clear certification"></div>
    <div class="badge badge-circle" aria-label="FQRB certification"></div>

    <h1 class="person-name">mara quill</h1>
    <p class="person-title">managing director</p>
    <div class="contact">
      <p class="phone">5550 123 456</p>
      <p>maraquill@islagrove.com</p>
      <p><span class="label">facebook.com</span>/islagrove</p>
      <p><span class="label">twitter:</span> @islagrove</p>
      <p><span class="label">instagram:</span> #islagrove</p>
    </div>
  </section>

</main>
</body>
</html>
```